Business Cards & Stationery
Hollowmere Capital Group (Investment Firm)
Project: Business Cards & Stationery
Business Cards & Stationery  -
Creative Brief
Professional
Peter L. Vanstrom III
Registered Principal, OSJ
917 Larkspur Road Milbrook, WV 25418
peter.vanstrom@quillmark-example.com
www.HollowmereCapitalGroup-example.com
Also has to say (in smaller font): Securities and advisory services offered through Crestfield Ledger Corporation (CLC). Member TVORA/BQLX and a Registered Investment Advisor. Hollowmere Capital Group and CLC are separate and unrelated companies.
logo for Hollowmere Capital Group

```html
<!DOCTYPE html>
<html lang="en">
<head>
<meta charset="utf-8">
<title>Hollowmere Capital Group — Business Cards</title>
<link rel="stylesheet" href="https://fonts.googleapis.com/css2?family=Cinzel:wght@400;500&display=swap">
<style>
  :root {
    --navy: #1d3f7a;
    --royal: #2b3fd0;
    --royal-deep: #16238f;
    --ink: #333b48;
    --muted: #6a707a;
    --shade: #8f949c;
    --card-edge: #7d7d7d;
    --paper: #ffffff;
  }
  * { margin: 0; padding: 0; box-sizing: border-box; }
  html, body { width: 1200px; height: 785px; overflow: hidden; background: var(--paper); }
  body { position: relative; font-family: "Cinzel", Georgia, serif; }

  .card {
    position: absolute;
    width: 564px; height: 324px;
    border: 1.5px solid var(--card-edge);
    border-radius: 22px;
    overflow: hidden;
    background: var(--paper);
  }
  .card--front { left: 24px; top: 60px; }
  .card--back  { left: 610px; top: 60px; border-color: var(--royal-deep);
                 background: radial-gradient(ellipse at 50% 50%, #3d55f0 0%, var(--royal) 40%, var(--royal-deep) 100%); }
  .card--plain { left: 316px; top: 400px; }

  .swoosh { position: absolute; inset: 0; width: 100%; height: 100%; }

  .brand { position: absolute; display: flex; align-items: center; gap: 14px; color: var(--navy); font-weight: 500; }
  .brand__mark { width: 50px; height: 50px; background: var(--navy); flex: none; }
  .brand__name { display: flex; flex-direction: column; line-height: 1; white-space: nowrap; }
  .brand__main { font-size: 28px; letter-spacing: 0.5px; }
  .brand__sub { font-size: 14px; letter-spacing: 5px; margin-top: 8px; }
  .brand--light { color: var(--paper); }
  .brand--light .brand__mark { background: var(--paper); }

  .card--front .brand { left: 24px; top: 24px; }
  .card--back .brand,
  .card--plain .brand { left: 50%; top: 50%; transform: translate(-50%, -50%); }

  .person { position: absolute; left: 120px; top: 150px; text-align: center; width: 300px; }
  .person__name { font-size: 24px; color: var(--navy); font-weight: 400; white-space: nowrap; }
  .person__title { font-size: 13px; color: var(--ink); margin-top: 4px; letter-spacing: 0.3px; }

  .contact { position: absolute; left: 18px; top: 214px; font-size: 12.5px; line-height: 17px; color: var(--ink); font-style: normal; }
  .contact__web { color: var(--navy); }

  .disclaimer {
    position: absolute; left: 22px; bottom: 16px; width: 380px;
    font-size: 8.5px; line-height: 12px; color: var(--muted);
  }
</style>
</head>
<body>

  <section class="card card--front" aria-label="Business card front">
    <svg class="swoosh" viewBox="0 0 564 324" preserveAspectRatio="none" aria-hidden="true">
      <defs>
        <linearGradient id="swoosh-front" x1="0" y1="1" x2="1" y2="0">
          <stop offset="0" stop-color="#16238f"/>
          <stop offset="1" stop-color="#3448e0"/>
        </linearGradient>
      </defs>
      <path d="M300 324 C430 305 530 220 564 95 L564 324 Z" fill="var(--shade)" opacity="0.55"/>
      <path d="M335 324 C450 305 540 230 564 120 L564 324 Z" fill="url(#swoosh-front)"/>
    </svg>
    <div class="brand">
      <span class="brand__mark"></span>
      <span class="brand__name"><span class="brand__main">Hollowmere</span><span class="brand__sub">Capital Group</span></span>
    </div>
    <div class="person">
      <h1 class="person__name">Peter L. Vanstrom III</h1>
      <p class="person__title">Registered Principal, OSJ</p>
    </div>
    <address class="contact">
      917 Larkspur Road<br>
      Milbrook, WV 25418<br>
      Phone: 304.555.0142 | Fax: 304.555.0187<br>
      Email: peter.vanstrom@quillmark-example.com<br>
      <span class="contact__web">www.HollowmereCapitalGroup-example.com</span>
    </address>
  </section>

  <section class="card card--back" aria-label="Business card back">
    <div class="brand brand--light">
      <span class="brand__mark"></span>
      <span class="brand__name"><span class="brand__main">Hollowmere</span><span class="brand__sub">Capital Group</span></span>
    </div>
  </section>

  <section class="card card--plain" aria-label="Business card, logo side">
    <svg class="swoosh" viewBox="0 0 564 324" preserveAspectRatio="none" aria-hidden="true">
      <defs>
        <linearGradient id="swoosh-plain" x1="0" y1="1" x2="1" y2="0">
          <stop offset="0" stop-color="#16238f"/>
          <stop offset="1" stop-color="#3448e0"/>
        </linearGradient>
      </defs>
      <path d="M400 324 C480 300 548 200 564 70 L564 324 Z" fill="var(--shade)" opacity="0.55"/>
      <path d="M430 324 C500 300 555 210 564 100 L564 324 Z" fill="url(#swoosh-plain)"/>
    </svg>
    <div class="brand">
      <span class="brand__mark"></span>
      <span class="brand__name"><span class="brand__main">Hollowmere</span><span class="brand__sub">Capital Group</span></span>
    </div>
    <p class="disclaimer">Securities and advisory services offered through Crestfield Ledger Corporation (CLC). Member TVORA/BQLX and a Registered Investment Advisor. Hollowmere Capital Group and CLC are separate and unrelated companies.</p>
  </section>

</body>
</html>
```